Room Hire at The Willowmere Wellbeing & Talking House to encourage therapists to hire rooms from us

An A4 page for magazine printing and use to send online as well.

We want to attract therapists to come and hire our beautiful rooms. We have a soft green, cream and brown colour theme and a professional, warm, elegant style (we hope)
I've uploaded the previous advert we had done through art bazaar which was aimed at attracting therapy clients.

Target Market(s)

psychotherapists and physical therapists searching to hire consulting rooms

Industry/Entity Type

Font styles to use
Serif
Sans Serif
Script
Other font styles liked:
• Good Vibes

Colors
cadf82
abd037
9bcb3c
fdf9ce
fff3d1

Requirements
Must have
• Please include this text
• Website address
• Contact email address
• "The rooms are available to hire all day into the evenings and at weekends.
• There are 8 rooms, all suitable for Couples work, Individual Counselling or Supervision sessions. Some rooms are designed to be used by physical therapists as well. One of them is large enough to use for Family Therapy, to hold groups or to run Training Sessions for approximately fourteen people."
• The colour scheme to harmonise with our website theme colours and fonts - Colour RGA numbers
• Brown
• Red 65
• Green 53
• Blue 53
• Light green
• Red 129
• Green 157
• Blue 115
• www.wmth-harbridge.example.co.uk.
• Scrolling writing is Good Vibes by Plinko
• Be warm, calm, welcoming, professional styling, striking.
Nice to have
• Pictures of our rooms if we can provide enough quality for printing
Should not have
• Pictures of people touching each other.
• Not be too busy or angular

```html
<!DOCTYPE html>
<html lang="en">
<head>
<meta charset="utf-8">
<title>Room Hire – The Willowmere Wellbeing &amp; Talking House</title>
<link rel="stylesheet" href="https://fonts.googleapis.com/css2?family=Great+Vibes&family=Montserrat:wght@500;600;700&display=swap">
<style>
  :root{
    --brown:#413535;
    --green:#9bcb3c;
    --green-bright:#abd037;
    --green-soft:#cadf82;
    --green-muted:#819d73;
    --cream:#fbf6e2;
    --cream-warm:#fff3d1;
    --page-bg:#e6e6e6;
  }
  *{box-sizing:border-box;margin:0;padding:0}
  html,body{width:1200px;height:1000px;overflow:hidden}
  body{background:var(--page-bg);font-family:"Montserrat",sans-serif;color:var(--brown)}
  .flyer{position:absolute;left:270px;top:33px;width:660px;height:934px;background:var(--cream);overflow:hidden;box-shadow:0 4px 18px rgba(0,0,0,.12)}
  .flyer-art{position:absolute;inset:0}
  .brand{position:absolute;left:0;right:0;top:58px;display:flex;align-items:center;justify-content:center;gap:12px}
  .brand-dot{width:18px;height:18px;border-radius:50%;background:var(--green)}
  .brand-name{font-weight:600;font-size:19px;color:var(--brown);letter-spacing:.2px}
  .contact{position:absolute;left:34px;top:556px;width:214px;text-align:right}
  .contact-hours{font-size:12px;font-weight:700;line-height:1.3}
  .contact-phone{font-size:27px;font-weight:700;margin-top:8px;letter-spacing:.3px;white-space:nowrap}
  .contact-email{font-size:11.5px;font-weight:700;line-height:1.6;margin-top:8px;text-align:left;white-space:nowrap}
  .headline{position:absolute;left:278px;top:660px;width:370px;font-family:"Great Vibes",cursive;font-weight:400;font-size:27px;line-height:1.15;color:var(--brown)}
  .details{position:absolute;left:272px;top:730px;width:370px;font-size:12px;font-weight:600;line-height:1.42}
  .details .highlight{color:var(--green)}
  .address{position:absolute;left:34px;top:862px;font-size:12px;font-weight:600;color:var(--cream)}
  .website{position:absolute;right:30px;top:892px;font-size:20px;font-weight:700;color:var(--green)}
</style>
</head>
<body>
<main class="flyer">
  <svg class="flyer-art" viewBox="0 0 660 934" width="660" height="934">
    <defs>
      <linearGradient id="room-main" x1="0" y1="0" x2="1" y2="1">
        <stop offset="0" stop-color="#d9cba3"/>
        <stop offset=".55" stop-color="#8a5a3c"/>
        <stop offset="1" stop-color="#5c4636"/>
      </linearGradient>
      <linearGradient id="room-small" x1="0" y1="0" x2="0" y2="1">
        <stop offset="0" stop-color="#e9e0c6"/>
        <stop offset="1" stop-color="#7c6a50"/>
      </linearGradient>
    </defs>

    <g class="room-photo-main" role="img" aria-label="Photo of a consulting room with a leather armchair, cabinet and fireplace">
      <rect x="0" y="140" width="480" height="440" fill="url(#room-main)"/>
    </g>

    <rect class="gallery-panel" x="470" y="190" width="190" height="400" fill="var(--green)"/>
    <g class="room-photo" role="img" aria-label="Photo of a room with dark armchairs and a coffee table">
      <rect x="484" y="222" width="166" height="112" rx="12" fill="url(#room-small)"/>
    </g>
    <g class="room-photo" role="img" aria-label="Photo of a room with cream armchairs and a window">
      <rect x="484" y="346" width="166" height="112" rx="12" fill="url(#room-small)"/>
    </g>
    <g class="room-photo" role="img" aria-label="Photo of a large room with armchairs and shelving">
      <rect x="484" y="470" width="166" height="112" rx="12" fill="url(#room-small)"/>
    </g>

    <path class="header-field" d="M0 0 H660 V222 C450 248 200 232 0 128 Z" fill="var(--cream)"/>
    <path class="header-swoosh" d="M0 130 C200 236 450 250 660 224" fill="none" stroke="var(--green-bright)" stroke-width="12"/>

    <path class="lower-swoosh" d="M0 562 C220 512 430 532 660 602" fill="none" stroke="var(--green-bright)" stroke-width="10"/>
    <path class="lower-band" d="M0 574 C220 524 430 544 660 614 V652 C430 578 220 556 0 602 Z" fill="var(--brown)"/>
    <path class="lower-field" d="M0 600 C220 554 430 576 660 650 V934 H0 Z" fill="var(--cream)"/>

    <rect class="contact-panel" x="22" y="530" width="240" height="296" rx="24" fill="var(--green-soft)" opacity=".95"/>

    <rect class="footer-rule" x="0" y="832" width="660" height="6" fill="var(--green-muted)"/>
    <rect class="footer-band" x="0" y="842" width="660" height="92" fill="var(--brown)"/>
  </svg>

  <header class="brand">
    <span class="brand-dot"></span>
    <span class="brand-name">The Willowmere Wellbeing &amp; Talking House</span>
  </header>

  <section class="contact">
    <p class="contact-hours">Appointments available<br>throughout the day and evening</p>
    <p class="contact-phone">01632 960418</p>
    <p class="contact-email">maren@wmth.example.co.uk<br>elspeth@wmth.example.co.uk</p>
  </section>

  <h1 class="headline">The rooms are available to hire all day into the Evenings and at Weekends.</h1>

  <p class="details">There are <span class="highlight">8 rooms, all suitable for Couples work, Individual Counselling or Supervision sessions.</span> Some rooms are designed to be used by physical therapists as well. One of them is large enough to use for Family Therapy, to hold groups or to run Training Sessions for approximately fourteen people.</p>

  <footer>
    <p class="address">14 Meadow Lane, Old Quarter, Harbridge HB2 7QT</p>
    <p class="website">www.wmth-harbridge.example.co.uk</p>
  </footer>
</main>
</body>
</html>
```